Pinecrest Valley Armory Banner

We are looking for a banner ad that we will run on DawnLedger.com the size is 758x120 and also a matching one that is 300x250 can be animated or static.final graphics will need to be submitted in jpg, gif or similar format. Our shop is a firearms business called "Pinecrest Valley Armory" located at 412 Route 19 South, Fernhill Vl. 20417 phone is 555-574-3186 . it need to be modern and eye catching and be more geared to the tactical side. Our website is
pinecrestarmory.com the banners DO NOT have to match website. would like a DIFFERENT LOOK than my website

```html
<!DOCTYPE html>
<html lang="en">
<head>
<meta charset="utf-8">
<title>Pinecrest Valley Armory Banners</title>
<link rel="stylesheet" href="https://fonts.googleapis.com/css2?family=Lato:wght@400;700;900&display=swap">
<style>
  :root {
    --stage: #575b57;
    --forest: #232b25;
    --navy: #00305e;
    --gold: #ffcc00;
    --sky: #4fb3e6;
    --ink: #111111;
    --white: #ffffff;
  }
  * { margin: 0; padding: 0; box-sizing: border-box; }
  html, body { width: 1200px; height: 1000px; overflow: hidden; }
  body { background: var(--stage); font-family: "Lato", Arial, sans-serif; position: relative; }

  .banner { position: absolute; overflow: hidden; box-shadow: 1px 1px 2px rgba(0,0,0,.35); }
  .banner svg.shapes { position: absolute; inset: 0; }
  .banner.forest { --base: var(--forest); }
  .banner.navy { --base: var(--navy); }

  .banner--square { width: 336px; height: 281px; top: 177px; }
  .banner--leader { width: 758px; height: 120px; left: 240px; }

  .brand { position: absolute; display: flex; align-items: center; gap: 7px; }
  .brand__dot { width: 40px; height: 40px; border-radius: 50%; background: var(--gold); flex: none; }
  .brand__name { color: var(--gold); font-weight: 700; font-size: 15px; line-height: 1.05; width: 112px; }

  .headline { position: absolute; text-align: center; color: var(--ink); font-weight: 700; line-height: 1;
    text-shadow: 1px 2px 2px rgba(0,0,0,.45); }
  .headline .lead { display: block; }

  .contact { position: absolute; color: var(--white); font-size: 12.5px; white-space: nowrap; }
  .contact .label { color: var(--sky); font-weight: 700; letter-spacing: .5px; }
  .contact .city { color: var(--sky); }
  .contact.spaced { letter-spacing: 1px; }
</style>
</head>
<body>

<!-- Square banner, forest -->
<div class="banner banner--square forest" style="left:240px;">
  <svg class="shapes" width="336" height="281" viewBox="0 0 336 281">
    <defs>
      <linearGradient id="photoA" x1="0" y1="0" x2="1" y2="1">
        <stop offset="0" stop-color="#f4f4f4"/><stop offset="0.45" stop-color="#5d6166"/><stop offset="0.7" stop-color="#2a2d31"/><stop offset="1" stop-color="#e8e8e8"/>
      </linearGradient>
    </defs>
    <rect width="336" height="281" fill="var(--base)"/>
    <polygon points="0,120 260,95 260,230 0,230" fill="var(--gold)"/>
    <path d="M238,0 Q140,115 190,230 L336,230 L336,0 Z" fill="var(--white)"/>
    <path d="M250,0 Q152,115 202,230 L336,230 L336,0 Z" fill="url(#photoA)" role="img" aria-label="Close-up photo of a handgun and magazine"/>
    <rect y="230" width="336" height="51" fill="var(--base)"/>
  </svg>
  <div class="brand" style="left:12px;top:28px;"><span class="brand__dot"></span><span class="brand__name">Pinecrest Valley Armory</span></div>
  <div class="headline" style="left:10px;top:134px;width:160px;">
    <span class="lead" style="font-size:29px;">Pinecrest</span>
    <span class="lead" style="font-size:23px;">Valley</span>
    <span class="lead" style="font-size:23px;">Armory</span>
  </div>
  <div class="contact" style="left:4px;top:239px;"><span class="label">ADRESS:</span> 412 Route 19 South, / <span class="city">Fernhill Vl. 20417</span></div>
  <div class="contact spaced" style="left:6px;top:261px;"><span class="label">PHONE:</span> 555-574-3186 <span class="label" style="font-size:10px;">WEB:</span> <span style="font-size:10.5px;">pinecrestarmory.com</span></div>
</div>

<!-- Square banner, navy -->
<div class="banner banner--square navy" style="left:619px;">
  <svg class="shapes" width="336" height="281" viewBox="0 0 336 281">
    <defs>
      <linearGradient id="photoB" x1="0" y1="0" x2="1" y2="1">
        <stop offset="0" stop-color="#f4f4f4"/><stop offset="0.45" stop-color="#5d6166"/><stop offset="0.7" stop-color="#2a2d31"/><stop offset="1" stop-color="#e8e8e8"/>
      </linearGradient>
    </defs>
    <rect width="336" height="281" fill="var(--base)"/>
    <polygon points="0,120 260,95 260,230 0,230" fill="var(--gold)"/>
    <path d="M238,0 Q140,115 190,230 L336,230 L336,0 Z" fill="var(--white)"/>
    <path d="M250,0 Q152,115 202,230 L336,230 L336,0 Z" fill="url(#photoB)" role="img" aria-label="Close-up photo of a handgun and magazine"/>
    <rect y="230" width="336" height="51" fill="var(--base)"/>
  </svg>
  <div class="brand" style="left:12px;top:28px;"><span class="brand__dot"></span><span class="brand__name">Pinecrest Valley Armory</span></div>
  <div class="headline" style="left:10px;top:134px;width:160px;">
    <span class="lead" style="font-size:29px;">Pinecrest</span>
    <span class="lead" style="font-size:23px;">Valley</span>
    <span class="lead" style="font-size:23px;">Armory</span>
  </div>
  <div class="contact" style="left:4px;top:239px;"><span class="label">ADRESS:</span> 412 Route 19 South, / <span class="city">Fernhill Vl. 20417</span></div>
  <div class="contact spaced" style="left:6px;top:261px;"><span class="label">PHONE:</span> 555-574-3186 <span class="label" style="font-size:10px;">WEB:</span> <span style="font-size:10.5px;">pinecrestarmory.com</span></div>
</div>

<!-- Leaderboard, forest -->
<div class="banner banner--leader forest" style="top:529px;">
  <svg class="shapes" width="758" height="120" viewBox="0 0 758 120">
    <defs>
      <linearGradient id="photoC" x1="0" y1="0" x2="1" y2="0">
        <stop offset="0" stop-color="#f4f4f4"/><stop offset="0.3" stop-color="#6a6e73"/><stop offset="0.55" stop-color="#2f3236"/><stop offset="0.8" stop-color="#8a8d91"/><stop offset="1" stop-color="#f4f4f4"/>
      </linearGradient>
    </defs>
    <rect width="758" height="120" fill="var(--gold)"/>
    <polygon points="0,0 235,0 220,100 0,100" fill="var(--base)"/>
    <path d="M470,0 Q430,60 452,120 L758,120 L758,0 Z" fill="url(#photoC)" role="img" aria-label="Photo of a handgun resting on a magazine"/>
    <path d="M0,100 H735 Q748,100 744,110 Q740,120 728,120 H0 Z" fill="var(--base)"/>
  </svg>
  <div class="brand" style="left:10px;top:20px;"><span class="brand__dot"></span><span class="brand__name" style="width:130px;font-size:16px;">Pinecrest Valley Armory</span></div>
  <div class="headline" style="left:228px;top:20px;width:216px;">
    <span class="lead" style="font-size:28px;">Pinecrest</span>
    <span class="lead" style="font-size:22px;">Valley Armory</span>
  </div>
  <div class="contact" style="left:7px;top:101px;"><span class="label">ADRESS:</span> 412 Route 19 South, / <span class="city">Fernhill Vl. 20417</span></div>
  <div class="contact spaced" style="left:351px;top:101px;"><span class="label">PHONE:</span> 555-574-3186</div>
  <div class="contact spaced" style="left:530px;top:101px;"><span class="label">WEB:</span> pinecrestarmory.com</div>
</div>

<!-- Leaderboard, navy -->
<div class="banner banner--leader navy" style="top:687px;">
  <svg class="shapes" width="758" height="120" viewBox="0 0 758 120">
    <defs>
      <linearGradient id="photoD" x1="0" y1="0" x2="1" y2="0">
        <stop offset="0" stop-color="#f4f4f4"/><stop offset="0.3" stop-color="#6a6e73"/><stop offset="0.55" stop-color="#2f3236"/><stop offset="0.8" stop-color="#8a8d91"/><stop offset="1" stop-color="#f4f4f4"/>
      </linearGradient>
    </defs>
    <rect width="758" height="120" fill="var(--gold)"/>
    <polygon points="0,0 235,0 220,100 0,100" fill="var(--base)"/>
    <path d="M470,0 Q430,60 452,120 L758,120 L758,0 Z" fill="url(#photoD)" role="img" aria-label="Photo of a handgun resting on a magazine"/>
    <path d="M0,100 H735 Q748,100 744,110 Q740,120 728,120 H0 Z" fill="var(--base)"/>
  </svg>
  <div class="brand" style="left:10px;top:20px;"><span class="brand__dot"></span><span class="brand__name" style="width:130px;font-size:16px;">Pinecrest Valley Armory</span></div>
  <div class="headline" style="left:228px;top:20px;width:216px;">
    <span class="lead" style="font-size:28px;">Pinecrest</span>
    <span class="lead" style="font-size:22px;">Valley Armory</span>
  </div>
  <div class="contact" style="left:7px;top:101px;"><span class="label">ADRESS:</span> 412 Route 19 South, / <span class="city">Fernhill Vl. 20417</span></div>
  <div class="contact spaced" style="left:351px;top:101px;"><span class="label">PHONE:</span> 555-574-3186</div>
  <div class="contact spaced" style="left:530px;top:101px;"><span class="label">WEB:</span> pinecrestarmory.com</div>
</div>

</body>
</html>
```